Seller Looking for a luxurious diverse ethnic look...stunning but not overly seductive

I need a web Design for a company based in NEW YORK CITY called Torvane Crest LLC. Initially I will be selling clothing and accessories as well as electronics on Quibra and hope to branch out. I want the whole experience for my customers and people I will buy from when they deal with me to be confident that this will be a torvane crest and luxurious transaction.
Updates

Project Deadline Extended Reason: As I keep getting these great designs I continue to get more ideas and feel more time will help get us there. Added Thursday, July 16, 2015

Target Market(s)

ages 20-60

Industry/Entity Type

Clothing

Number of Pages Required

1 page

Font styles to use
Script

Colors
b768aa

Requirements
Must have
• Sleek and Luxurious feel and modern. I would like the page to look startling stunning yet not overly seductive and to include ethnic diversity. I like the illusion not knowing what the sight is selling since I am not targeting one area.
Should not have
• Do not want it to look generic or traditional

```html
<!DOCTYPE html>
<html lang="en">
<head>
<meta charset="UTF-8">
<title>Torvane Crest LLC</title>
<link href="https://fonts.googleapis.com/css2?family=Open+Sans:wght@400;600;700&family=Oswald:wght@500;700&display=swap" rel="stylesheet">
<style>
:root{
  --brand:#b768aa;
  --brand-dark:#8e4a84;
  --brand-deep:#6d3566;
  --ink:#333333;
  --muted:#777777;
  --line:#dddddd;
  --white:#ffffff;
  --dark:#2b2327;
}
*{box-sizing:border-box;margin:0;padding:0}
html,body{width:1200px;height:2436px;overflow:hidden}
body{font-family:"Open Sans",Arial,sans-serif;color:var(--ink);background:var(--white);font-size:13px;line-height:1.6}
.heading{font-family:"Oswald","Arial Narrow",sans-serif;font-weight:700;text-transform:uppercase;letter-spacing:1px}
.rule{width:40px;height:3px;background:var(--brand);margin:10px 0 18px}
.btn{display:inline-block;background:var(--brand);color:var(--white);font-size:12px;padding:9px 22px;border-radius:2px}

/* header */
.site-header{height:64px;display:flex;align-items:center;justify-content:space-between;padding:0 230px 0 270px;background:var(--white)}
.brand-name{font-size:20px;font-weight:600;color:var(--brand-deep)}
.main-nav{display:flex;align-items:center;gap:4px;font-size:12px}
.main-nav span{padding:6px 10px;color:var(--ink)}
.main-nav .active{background:var(--brand);color:var(--white)}

/* hero */
.hero{position:relative;height:496px;overflow:hidden}
.hero-photo{position:absolute;inset:0;background:linear-gradient(100deg,#6b5f66 0%,#9a8d96 40%,#c9b7b4 70%,#7c6a6f 100%)}
.hero-shade{position:absolute;inset:0;background:rgba(40,20,35,.35)}
.hero-copy{position:absolute;left:270px;top:170px;width:560px;color:var(--white)}
.hero-copy h1{font-size:36px;margin-bottom:14px}
.hero-copy p{font-size:13px;margin-bottom:28px;opacity:.95}
.hero-dots{position:absolute;left:0;right:0;bottom:22px;display:flex;justify-content:center;gap:8px}
.hero-dots i{width:9px;height:9px;border-radius:50%;background:rgba(255,255,255,.55)}
.hero-dots i:first-child{background:var(--white)}

/* about */
.about{height:380px;display:flex;align-items:center;gap:50px;padding:0 230px 0 150px}
.about-art{width:370px;height:340px;background:radial-gradient(circle at 50% 50%,#e6e9f2 0%,#c7d3e6 45%,#ffffff 75%)}
.about-text{flex:1}
.about-text h2{font-size:22px}
.about-text p{font-size:12px;color:var(--muted);margin-bottom:12px}
.about-text strong{color:var(--ink)}

/* stats */
.stats{height:210px;background:linear-gradient(90deg,var(--brand-dark),var(--brand) 50%,var(--brand-dark));display:flex;justify-content:center;align-items:center;gap:16px}
.stat{width:180px;height:92px;background:var(--white);text-align:center;padding-top:6px}
.stat b{display:block;font-family:"Oswald",sans-serif;font-size:44px;line-height:1.1;color:var(--ink)}
.stat small{font-size:9px;font-weight:700;color:var(--ink);text-transform:uppercase}

/* products */
.products{position:relative;height:410px;overflow:hidden}
.products-photo{position:absolute;inset:0;background:linear-gradient(120deg,#3a2f33,#5a4a4c 50%,#2e2629)}
.products-inner{position:relative;text-align:center;padding-top:22px;color:var(--white)}
.products-inner h2{font-size:22px}
.products-inner .rule{margin:8px auto 20px;background:var(--white)}
.product-grid{display:flex;justify-content:center;gap:6px}
.product{width:180px;text-align:left}
.product-photo{height:105px}
.product-body{background:var(--brand);padding:12px 14px;height:140px;color:var(--white)}
.product-body h3{font-size:13px;font-family:"Oswald",sans-serif;font-weight:500;text-align:center;margin-bottom:8px;letter-spacing:1px}
.product-body p{font-size:10.5px;line-height:1.5;text-align:center}

/* contact */
.contact{height:580px;text-align:center;padding-top:48px}
.contact h2{font-size:24px}
.contact .rule{margin:8px auto 16px}
.contact-lead{width:560px;margin:0 auto 24px;font-size:11px;color:var(--muted)}
.contact-info{display:flex;justify-content:center;gap:70px;margin-bottom:30px;text-align:left;font-size:11px;color:var(--muted)}
.contact-info div{display:flex;gap:8px;align-items:flex-start}
.contact-form{width:730px;margin:0 auto;text-align:left}
.field{border:1px solid var(--line);height:28px;font-size:11px;color:#999;padding:5px 10px;margin-bottom:10px}
.row{display:flex;gap:10px}
.row .field{flex:1}
.field.message{height:140px}

/* footer */
.site-footer{height:296px;background:linear-gradient(100deg,var(--brand-deep),var(--brand) 50%,var(--brand-dark));color:var(--white);position:relative}
.footer-cols{display:flex;padding:40px 230px 0 235px;gap:60px}
.footer-col h4{font-size:15px;font-family:"Oswald",sans-serif;font-weight:500;text-transform:uppercase}
.footer-col .rule{background:var(--white);margin:6px 0 12px}
.footer-col p,.footer-col li{font-size:11px;list-style:none;line-height:1.8}
.about-col{width:290px}
.map-col{width:200px}
.social{display:flex;gap:6px;margin-top:14px}
.social i{width:22px;height:22px;background:var(--white)}
.footer-bar{position:absolute;left:0;right:0;bottom:0;height:32px;background:rgba(0,0,0,.18);font-size:10px;padding:8px 235px}
</style>
</head>
<body>

<header class="site-header">
  <div class="brand-name">Torvane Crest LLC</div>
  <nav class="main-nav">
    <span class="active">Home</span><span>About Us</span><span>Services</span><span>Products</span><span>Blog</span><span>Contact Us</span>
    <svg width="14" height="14" viewBox="0 0 14 14"><circle cx="6" cy="6" r="4.5" fill="none" stroke="#333" stroke-width="1.6"/><line x1="9.3" y1="9.3" x2="13" y2="13" stroke="#333" stroke-width="1.6"/></svg>
  </nav>
</header>

<section class="hero">
  <div class="hero-photo" role="img" aria-label="Woman shopping in a clothing boutique, looking at her phone"></div>
  <div class="hero-shade"></div>
  <div class="hero-copy">
    <h1 class="heading">Lorem ipsum dolor sit amet.</h1>
    <p>Lorem ipsum dolor sit amet, consectetur adipiscing elit. Integer posuere erat a ante venenatis dapibus posuere velit aliquet. Donec sed odio dui, cras mattis consectetur purus sit amet fermentum.</p>
    <span class="btn">Get Started Now</span>
  </div>
  <div class="hero-dots"><i></i><i></i><i></i></div>
</section>

<section class="about">
  <div class="about-art" role="img" aria-label="Illustration of a smartphone surrounded by shopping and app icons"></div>
  <div class="about-text">
    <h2 class="heading">About Us</h2>
    <div class="rule"></div>
    <p><strong>Torvane Crest LLC</strong> — Lorem ipsum dolor sit amet, consectetur adipiscing elit. Aenean commodo ligula eget dolor massa, cum sociis natoque penatibus et magnis dis parturient montes nascetur ridiculus.</p>
    <p>Donec quam felis, ultricies nec pellentesque eu, pretium quis sem. Nulla consequat massa quis enim. Donec pede justo, fringilla vel aliquet nec, vulputate eget arcu. In enim justo, rhoncus ut imperdiet a, venenatis vitae justo.</p>
    <span class="btn">Read More</span>
  </div>
</section>

<section class="stats">
  <div class="stat"><b>7</b><small>Years of Business</small></div>
  <div class="stat"><b>10</b><small>Years Experience</small></div>
  <div class="stat"><b>10+</b><small>Retail Stores</small></div>
  <div class="stat"><b>5000</b><small>Satisfied Customers</small></div>
</section>

<section class="products">
  <div class="products-photo" role="img" aria-label="Dimmed background of fashion accessories on a table"></div>
  <div class="products-inner">
    <h2 class="heading">Our Products</h2>
    <div class="rule"></div>
    <div class="product-grid">
      <div class="product">
        <div class="product-photo" role="img" aria-label="Men's clothing" style="background:linear-gradient(135deg,#c9c2bd,#8f857f)"></div>
        <div class="product-body"><h3>MEN'S WEAR</h3><p>Lorem ipsum dolor sit amet, consectetur adipiscing elit sed do eiusmod tempor incididunt ut labore.</p></div>
      </div>
      <div class="product">
        <div class="product-photo" role="img" aria-label="Women's clothing on a rack" style="background:linear-gradient(135deg,#d56b8f,#3f6fa8)"></div>
        <div class="product-body"><h3>WOMEN'S WEAR</h3><p>Lorem ipsum dolor sit amet, consectetur adipiscing elit sed do eiusmod tempor incididunt ut labore.</p></div>
      </div>
      <div class="product">
        <div class="product-photo" role="img" aria-label="Jewelry and accessories" style="background:linear-gradient(135deg,#f1d4d8,#d9a7b2)"></div>
        <div class="product-body"><h3>ACCESSORIES</h3><p>Lorem ipsum dolor sit amet, consectetur adipiscing elit sed do eiusmod tempor incididunt ut labore.</p></div>
      </div>
      <div class="product">
        <div class="product-photo" role="img" aria-label="Consumer electronics devices" style="background:linear-gradient(135deg,#9fb7c9,#d9c99a)"></div>
        <div class="product-body"><h3>ELECTRONICS</h3><p>Lorem ipsum dolor sit amet, consectetur adipiscing elit sed do eiusmod tempor incididunt ut labore.</p></div>
      </div>
    </div>
  </div>
</section>

<section class="contact">
  <h2 class="heading">Contact Us</h2>
  <div class="rule"></div>
  <p class="contact-lead">Lorem ipsum dolor sit amet, consectetur adipiscing elit. Nullam dictum felis eu pede mollis pretium. Integer tincidunt, cras dapibus vivamus elementum semper nisi aenean vulputate eleifend tellus.</p>
  <div class="contact-info">
    <div><svg width="14" height="18" viewBox="0 0 14 18"><path d="M7 1a6 6 0 0 0-6 6c0 4.5 6 10 6 10s6-5.5 6-10a6 6 0 0 0-6-6z" fill="#b768aa"/><circle cx="7" cy="7" r="2.2" fill="#fff"/></svg><span>148 Marlow Avenue<br>Suite 900<br>New York, NY 10001</span></div>
    <div><svg width="12" height="18" viewBox="0 0 12 18"><rect x="1" y="1" width="10" height="16" rx="2" fill="#b768aa"/><rect x="3" y="3" width="6" height="10" fill="#fff"/></svg><span>(212) 555-0148</span></div>
    <div><svg width="18" height="13" viewBox="0 0 18 13"><rect x="1" y="1" width="16" height="11" fill="#b768aa"/><path d="M1 1l8 6 8-6" fill="none" stroke="#fff" stroke-width="1.3"/></svg><span>hello@torvanecrest.com</span></div>
  </div>
  <div class="contact-form">
    <div class="row"><div class="field">Name</div><div class="field">Email</div></div>
    <div class="field">Subject</div>
    <div class="field message">Message</div>
    <span class="btn">Send</span>
  </div>
</section>

<footer class="site-footer">
  <div class="footer-cols">
    <div class="footer-col about-col">
      <h4>About Us</h4><div class="rule"></div>
      <p>Lorem ipsum dolor sit amet, consectetur adipiscing elit. Aenean commodo ligula eget dolor, aenean massa cum sociis natoque penatibus et magnis dis parturient.</p>
      <div class="social"><i></i><i></i><i></i><i></i></div>
    </div>
    <div class="footer-col map-col">
      <h4>Site Map</h4><div class="rule"></div>
      <ul><li>Home</li><li>About Us</li><li>Services</li><li>Products</li><li>Blog</li><li>Contact Us</li></ul>
    </div>
    <div class="footer-col">
      <h4>Contact Info</h4><div class="rule"></div>
      <p>148 Marlow Avenue<br>Suite 900<br>New York, NY 10001</p>
      <p style="margin-top:10px">hello@torvanecrest.com<br>(212) 555-0148</p>
    </div>
  </div>
  <div class="footer-bar">Copyright 2015 Torvane Crest LLC. All Rights Reserved.</div>
</footer>

</body>
</html>
```